Cybersecurity company is looking for business card.

I need a business card design for our company, we are a cybersecurity company providing advance technology to protect agains any kind of malware. We need a fresh modern design it should communicate modern, technology and growth.

Target Market(s)

Business to business

Industry/Entity Type

Business

Contact Information for Business Card

Should have location, address, fax, mobile, phone, email and website.

Requirements
Must have
• Must follow company's logo color and style. Must have the company's log on its.

```html
<!DOCTYPE html>
<html lang="en">
<head>
<meta charset="utf-8">
<title>Kyvora Business Card</title>
<link rel="stylesheet" href="https://fonts.googleapis.com/css2?family=Roboto+Condensed:wght@400;500;700;800&display=swap">
<style>
  :root {
    --stage: #2b2b2b;
    --card-light: #eeeeee;
    --card-mid: #dcdcdc;
    --ink: #0d0d0d;
    --brand-red: #a01c22;
    --label: #111111;
    --photo-light: #d9d6d4;
    --photo-mid: #bdbab8;
    --photo-warm: #e9b7a6;
  }
  * { margin: 0; padding: 0; box-sizing: border-box; }
  html, body { width: 1200px; height: 900px; overflow: hidden; }
  body {
    background: var(--stage);
    font-family: "Roboto Condensed", "Arial Narrow", sans-serif;
    position: relative;
  }
  .side-label {
    position: absolute;
    font-weight: 800;
    font-size: 26px;
    color: var(--label);
    background: #8a8a8a;
    padding: 0 4px;
    line-height: 28px;
  }
  .side-label--front { left: 55px; top: 10px; }
  .side-label--back { left: 1072px; top: 386px; }

  .card {
    position: absolute;
    width: 782px;
    height: 457px;
    overflow: hidden;
  }
  .card--back { left: 370px; top: 415px; z-index: 1; }
  .card--front {
    left: 54px; top: 44px; z-index: 2;
    background: radial-gradient(ellipse at 45% 40%, #f4f4f4 0%, var(--card-light) 55%, var(--card-mid) 100%);
  }

  .accent-band {
    position: absolute;
    left: 38px; top: 0;
    width: 39px; height: 96px;
    background: var(--brand-red);
  }
  .corner-accent {
    position: absolute;
    right: 0; bottom: 0;
    width: 194px; height: 221px;
    background: linear-gradient(160deg, rgba(160,28,34,0) 0%, rgba(160,28,34,0.85) 45%, var(--ink) 100%);
  }

  .wordmark {
    position: absolute;
    font-weight: 800;
    color: var(--ink);
    letter-spacing: 3px;
    line-height: 1;
  }
  .card--front .wordmark { right: 48px; top: 36px; font-size: 74px; }

  .contact-list {
    position: absolute;
    left: 58px;
    top: 232px;
    list-style: none;
    color: var(--ink);
    font-size: 16px;
    font-weight: 500;
    letter-spacing: 0.6px;
  }
  .contact-list li { line-height: 25.6px; }

  .backdrop-photo {
    position: absolute; inset: 0;
    background:
      radial-gradient(ellipse 28% 36% at 40% 50%, var(--photo-warm) 0%, rgba(233,183,166,0.6) 55%, rgba(233,183,166,0) 100%),
      linear-gradient(135deg, var(--photo-light) 0%, var(--photo-mid) 55%, var(--photo-light) 100%);
  }
  .card--back .wordmark {
    left: 132px; top: 162px; font-size: 112px; letter-spacing: 5px;
  }
</style>
</head>
<body>
  <span class="side-label side-label--front">front</span>
  <span class="side-label side-label--back">back</span>

  <section class="card card--back" aria-label="Card back">
    <div class="backdrop-photo" role="img" aria-label="Close-up of a keyboard with a glowing orange padlock key"></div>
    <div class="wordmark">kyvora</div>
  </section>

  <section class="card card--front" aria-label="Card front">
    <div class="accent-band"></div>
    <div class="corner-accent" role="img" aria-label="Red and black corner decoration"></div>
    <div class="wordmark">kyvora</div>
    <ul class="contact-list">
      <li>Location : Dubai - UAE</li>
      <li>Address: Harbor Tech Park (HTP) -Coral Bay Road.</li>
      <li>Mobile: +971 52 123 XXXX</li>
      <li>Phone: 04 123 XXXX</li>
      <li>Fax: 04 123 XXXX</li>
      <li>Email : name.surname@kyvora.com</li>
      <li>Website: www.kyvora.com</li>
    </ul>
  </section>
</body>
</html>
```